Harrow's Electrical & Solar - Business Cards

I want my business card to stand out from the rest. I will provide my business name logo and my icon logo to be implemented onto the card.

On the front of the card, can i have the following. Just make it neat & professional please.

Liam Corbett
harrowselectrical@quillmail.test
0438 917 605
ABN: 41 602 719 384
License No. 582164K
FREE QUOTES
24/7 Emergency

On the back of the card, can I have "Our Services" and maybe add the S logo on the back in the background or something. Under "Our Services" I want the following:

LED Lighting Upgrades
Switches & Outlets
Smoke Alarms
Switchboard Upgrades
Fault Finding
Rewiring
New Builds
Test & Tagging
All Electrical Maintenance & Repairs

Can you guys add the instagram logo and next to it, put harrows_electrical

Can you guys also add the facebook logo and next to it put Harrow's Electrical & Solar. Make sure the instagram & facebook icon is in either white, green or black.

Also I have put down double sided, not sure why when i save it, it keeps going to single sided. I need my business card double sided.

Target Market(s)

New Customers

Contact Information for Business Card

Liam Corbett harrowselectrical@quillmail.test 0438 917 605 ABN: 41 602 719 384 License No. 582164K FREE QUOTES 24/7 Emergency

Requirements
Must have
• must be tidy, professional and appealing

```html
<!DOCTYPE html>
<html lang="en">
<head>
<meta charset="utf-8">
<title>Harrow's Electrical &amp; Solar – Business Cards</title>
<link rel="stylesheet" href="https://fonts.googleapis.com/css2?family=Exo+2:ital,wght@0,400;0,500;0,700;1,800&display=swap">
<style>
  :root {
    --page: #2a2b2d;
    --card: #1b1c1e;
    --green: #3fc43a;
    --text: #f1f1f1;
    --muted: #c9c9c9;
    --rule: #4a4b4e;
  }
  * { margin: 0; padding: 0; box-sizing: border-box; }
  html, body { width: 1200px; height: 874px; overflow: hidden; }
  body {
    background: var(--page);
    font-family: "Exo 2", sans-serif;
    color: var(--text);
    position: relative;
  }
  .card {
    position: absolute;
    left: 270px;
    width: 660px;
    height: 400px;
    background: var(--card);
    border-radius: 22px;
    box-shadow: 0 10px 26px rgba(0,0,0,.45);
  }
  .card--back { top: 22px; }
  .card--front { top: 452px; }

  /* back side */
  .brand-mark {
    position: absolute; left: 0; right: 0; top: 30px;
    display: flex; flex-direction: column; align-items: center; gap: 12px;
  }
  .brand-mark__circle {
    width: 120px; height: 120px; border-radius: 50%;
    border: 9px solid var(--green);
  }
  .brand-mark__name {
    font-weight: 700; font-size: 17px; color: var(--text); letter-spacing: .5px;
  }
  .services {
    position: absolute; left: 30px; right: 30px; top: 212px;
    text-align: center; font-size: 18px; line-height: 25px; font-weight: 400;
  }
  .services .dot { color: var(--green); margin: 0 8px; }
  .socials {
    position: absolute; left: 40px; right: 40px; top: 312px;
    border-top: 1px solid var(--rule); padding-top: 14px;
    display: flex; justify-content: center; gap: 26px; font-size: 17px;
  }
  .socials__item { display: flex; align-items: center; gap: 8px; }
  .socials__dot { width: 13px; height: 13px; border-radius: 50%; background: var(--green); }

  /* front side */
  .wordmark {
    position: absolute; right: 44px; top: 110px;
    font-weight: 700; font-size: 28px; color: #d9d9d9; letter-spacing: .5px;
  }
  .contact {
    position: absolute; left: 48px; top: 214px; width: 572px;
  }
  .contact__name {
    font-weight: 800; font-style: italic; font-size: 30px; color: var(--green);
    text-transform: uppercase; letter-spacing: .5px;
    padding-bottom: 8px; border-bottom: 1px solid var(--rule);
  }
  .contact__list { list-style: none; margin-top: 10px; font-size: 19px; line-height: 28px; }
  .contact__list li { display: flex; align-items: center; gap: 10px; }
  .contact__list svg { width: 15px; height: 15px; fill: var(--green); }
  .offers {
    position: absolute; right: 60px; bottom: 34px; width: 240px;
    border-top: 1px solid var(--rule); padding-top: 12px;
    list-style: none; font-size: 19px; line-height: 27px; font-weight: 500;
  }
  .offers li::before { content: "•"; color: var(--green); margin-right: 12px; }
</style>
</head>
<body>
  <section class="card card--back" aria-label="Card back">
    <div class="brand-mark">
      <div class="brand-mark__circle"></div>
      <div class="brand-mark__name">Harrow's Electrical &amp; Solar</div>
    </div>
    <p class="services">
      LED Lighting Upgrades<span class="dot">•</span>Switches &amp; Outlets<span class="dot">•</span>Smoke Alarms<br>
      Switchboard Upgrades<span class="dot">•</span>Fault Finding<span class="dot">•</span>Rewiring<span class="dot">•</span>New Builds<br>
      Test &amp; Tagging<span class="dot">•</span>All Electrical Maintenance &amp; Repairs
    </p>
    <div class="socials">
      <span class="socials__item"><span class="socials__dot"></span>Harrow's Electrical &amp; Solar</span>
      <span class="socials__item"><span class="socials__dot"></span>harrows_electrical</span>
    </div>
  </section>

  <section class="card card--front" aria-label="Card front">
    <div class="wordmark">Harrow's Electrical &amp; Solar</div>
    <div class="contact">
      <h1 class="contact__name">Liam Corbett</h1>
      <ul class="contact__list">
        <li><svg viewBox="0 0 24 24" aria-hidden="true"><path d="M6.6 10.8a15 15 0 0 0 6.6 6.6l2.2-2.2a1 1 0 0 1 1-.25 11.4 11.4 0 0 0 3.6.57 1 1 0 0 1 1 1V20a1 1 0 0 1-1 1A17 17 0 0 1 3 4a1 1 0 0 1 1-1h3.5a1 1 0 0 1 1 1c0 1.25.2 2.45.57 3.57a1 1 0 0 1-.25 1z"/></svg>0438 917 605</li>
        <li><svg viewBox="0 0 24 24" aria-hidden="true"><path d="M2 5h20v14H2zm2 2v.5l8 5 8-5V7l-8 5z"/></svg>harrowselectrical@quillmail.test</li>
        <li>License No.582164K</li>
      </ul>
    </div>
    <ul class="offers">
      <li>FREE QUOTES</li>
      <li>24/7 Emergency</li>
    </ul>
  </section>
</body>
</html>
```